business card design

i would like business cards designed. My business provides trade qualified personnel to the mining industry to work on heavy mobile equipment.
please put a excavator(digger) in the background in one design and have one design without so i can compare the difference.
also add info:
my logo(attached) and "mobile equipment repair and maintenance"
name: Derek Holloway
address: 57 Tarrowby RD Kelwyn Dale WA.
mobile: 0438120957
email: derek@ironvalemx.com

```html
<!DOCTYPE html>
<html lang="en">
<head>
<meta charset="utf-8">
<title>Ironvale Business Cards</title>
<link rel="stylesheet" href="https://fonts.googleapis.com/css2?family=Montserrat:wght@400;500;800&display=swap">
<style>
  :root {
    --page: #e6e6e6;
    --navy-dark: #0e2248;
    --navy: #183a72;
    --navy-mid: #20478a;
    --accent: #4a7fd6;
    --white: #ffffff;
  }
  * { margin: 0; padding: 0; box-sizing: border-box; }
  html, body { width: 1200px; height: 1200px; overflow: hidden; }
  body {
    background: var(--page);
    font-family: "Montserrat", sans-serif;
    position: relative;
  }
  .card {
    position: absolute;
    left: 180px;
    width: 840px;
    height: 480px;
    overflow: hidden;
    color: var(--white);
  }
  .card--front { top: 68px; }
  .card--back { top: 652px; }
  .card__photo {
    position: absolute; inset: 0;
    background:
      radial-gradient(ellipse at 65% 55%, rgba(60,100,160,0.45), transparent 60%),
      linear-gradient(180deg, var(--navy) 0%, var(--navy-mid) 45%, var(--navy-dark) 100%);
  }
  .brand {
    position: absolute; left: 0; right: 0;
    text-align: center;
  }
  .brand__name {
    font-weight: 800;
    font-size: 90px;
    line-height: 1;
    letter-spacing: 6px;
    color: var(--white);
    transform: translateY(-50%);
  }
  .brand__sub {
    position: absolute; left: 0; right: 0;
    text-align: center;
    font-weight: 500;
    font-size: 22px;
    letter-spacing: 2.6px;
    color: var(--accent);
    transform: translateY(-50%);
  }
  .tagline {
    position: absolute; left: 0; right: 0;
    display: flex; justify-content: center; align-items: center; gap: 8px;
    font-weight: 500;
    font-size: 14.5px;
    letter-spacing: 0.8px;
    transform: translateY(-50%);
  }
  .tagline svg { width: 30px; height: 12px; }
  .contact {
    position: absolute;
    display: flex; align-items: center;
    font-size: 17px;
    letter-spacing: 0.4px;
    white-space: nowrap;
    transform: translateY(-50%);
  }
  .contact svg { width: 36px; height: 36px; margin-right: 18px; flex: none; }
</style>
</head>
<body>

<section class="card card--front">
  <div class="card__photo" role="img" aria-label="Excavator working at a mining site at dusk, dark blue toned"></div>

  <div class="brand" style="top:116px"><div class="brand__name">IRONVALE</div></div>
  <div class="brand__sub" style="top:168px">MAINTENANCE SERVICES PTY LTD</div>
  <div class="tagline" style="top:197px">
    <svg viewBox="0 0 30 12"><polygon points="6,0 15,0 9,12 0,12" fill="var(--accent)"/><polygon points="20,0 29,0 23,12 14,12" fill="var(--accent)"/></svg>
    <span>MOBILE EQUIPMENT REPAIR AND MAINTENANCE</span>
    <svg viewBox="0 0 30 12"><polygon points="1,0 10,0 16,12 7,12" fill="var(--accent)"/><polygon points="15,0 24,0 30,12 21,12" fill="var(--accent)"/></svg>
  </div>

  <div class="contact" style="left:122px; top:318px">
    <svg viewBox="0 0 36 36"><circle cx="18" cy="18" r="18" fill="#fff"/><circle cx="18" cy="14" r="6" fill="var(--navy)"/><path d="M8 28c2-6 6-8 10-8s8 2 10 8z" fill="var(--navy)"/></svg>
    <span>Derek Holloway</span>
  </div>
  <div class="contact" style="left:122px; top:378px">
    <svg viewBox="0 0 36 36"><circle cx="18" cy="18" r="18" fill="#fff"/><path d="M12 9l4 0 2 5-3 2c1 3 3 5 6 6l2-3 5 2 0 4c-1 2-3 2-5 2-7-1-13-7-14-14 0-2 1-4 3-4z" fill="var(--navy)"/></svg>
    <span>0438120957</span>
  </div>
  <div class="contact" style="left:389px; top:318px">
    <svg viewBox="0 0 36 36"><circle cx="18" cy="18" r="18" fill="#fff"/><rect x="9" y="12" width="18" height="12" fill="none" stroke="var(--navy)" stroke-width="2"/><path d="M9 12l9 7 9-7M9 24l7-6M27 24l-7-6" fill="none" stroke="var(--navy)" stroke-width="2"/></svg>
    <span>derek@ironvalemx.com</span>
  </div>
  <div class="contact" style="left:389px; top:378px">
    <svg viewBox="0 0 36 36"><circle cx="18" cy="18" r="18" fill="#fff"/><path d="M18 8a7 7 0 0 1 7 7c0 5-7 13-7 13s-7-8-7-13a7 7 0 0 1 7-7z" fill="var(--navy)"/><circle cx="18" cy="15" r="2.6" fill="#fff"/></svg>
    <span>57 Tarrowby RD Kelwyn Dale WA.</span>
  </div>
</section>

<section class="card card--back">
  <div class="card__photo" role="img" aria-label="Excavator working at a mining site at dusk, dark blue toned"></div>

  <div class="brand" style="top:214px"><div class="brand__name">IRONVALE</div></div>
  <div class="brand__sub" style="top:265px">MAINTENANCE SERVICES PTY LTD</div>
  <div class="tagline" style="top:294px">
    <svg viewBox="0 0 30 12"><polygon points="6,0 15,0 9,12 0,12" fill="var(--accent)"/><polygon points="20,0 29,0 23,12 14,12" fill="var(--accent)"/></svg>
    <span>MOBILE EQUIPMENT REPAIR AND MAINTENANCE</span>
    <svg viewBox="0 0 30 12"><polygon points="1,0 10,0 16,12 7,12" fill="var(--accent)"/><polygon points="15,0 24,0 30,12 21,12" fill="var(--accent)"/></svg>
  </div>
</section>

</body>
</html>
```